Tender Scout Letterhead Design Project

We need a letterhead design for a consultancy business based in Australia.

Tender Scout is a unique business designed to assist with the complex and time consuming nature of selecting contractors, showing them what to do and reviewing quotes when it comes to body corporate and strata maintenance items such as painting, waterproofing, plumbing and electrical.

Target Market(s)

apartment managers

Industry/Entity Type

Business

Requirements
Must have
• must have logo and contact details

Tender Scout
82 Wallaroo Creek Road
Yandara, QLD 4571
Ph 07 5391 2846
Fax 07 5327 6018
Mobile 0438 917304

```html
<!DOCTYPE html>
<html lang="en">
<head>
<meta charset="utf-8">
<title>Tender Scout Letterhead</title>
<link rel="stylesheet" href="https://fonts.googleapis.com/css2?family=Jost:wght@300;400&display=swap">
<style>
  :root {
    --paper: #ffffff;
    --brand-red: #e31e2d;
    --text-grey: #8a8c8f;
  }
  html, body {
    margin: 0;
    padding: 0;
    overflow: hidden;
    background: var(--paper);
  }
  .letterhead {
    position: relative;
    width: 848px;
    height: 1200px;
    background: var(--paper);
    overflow: hidden;
  }
  .corner-mark {
    position: absolute;
    left: 58px;
    top: 62px;
    width: 140px;
    height: 140px;
  }
  .footer-name {
    position: absolute;
    left: 0;
    right: 0;
    top: 1068px;
    margin: 0;
    text-align: center;
    font-family: "Jost", "Futura", sans-serif;
    font-weight: 400;
    font-size: 44px;
    line-height: 1;
    color: var(--text-grey);
  }
  .contact {
    position: absolute;
    left: 0;
    right: 0;
    top: 1158px;
    margin: 0;
    text-align: center;
    font-family: "Jost", "Futura", sans-serif;
    font-weight: 300;
    font-size: 15.5px;
    line-height: 19px;
    color: var(--text-grey);
    text-transform: uppercase;
    font-style: normal;
  }
  .contact-name {
    color: var(--brand-red);
    font-weight: 400;
    text-transform: none;
  }
</style>
</head>
<body>
  <main class="letterhead">
    <svg class="corner-mark" viewBox="0 0 140 140" aria-hidden="true">
      <circle cx="70" cy="70" r="70" fill="var(--brand-red)"/>
    </svg>

    <p class="footer-name">Tender Scout</p>

    <address class="contact">
      <span class="contact-name">Tender Scout</span> 82 Wallaroo Creek Road, Yandara, QLD 4571<br>
      Ph 07 5391 2846. Fax 07 5327 6018. Mobile 0438 917304
    </address>
  </main>
</body>
</html>
```